harvest Soon Book Cover Design for real estate investment book

I am looking for a Book Cover design for my new book. I would like designs for a hardcover, softcover and Lumora book.

The book deals with real estate and mortgage investments. Looking for a clean, bright simple design. Want to cover to be White with big RED letters. See "Dancing past Noon" book for an example ... see attached.

Target Market(s)

Affluent people with money looking for investment solutions.

Industry/Entity Type

Financial Service

Font styles to use
Serif

Requirements
Must have
• Bright clean design that will be appealing to affluent people.
• Title: harvest SOON
• Subtitle: A quiet method for thriving through land holdings
• subsubtitle: Secrets the Bank Teller Keeps Hidden From Clients...
• Author: Ned Falconby
• My Picture on the inside cover or on the back cover
• Book Description, Author description
Nice to have
• Focus on the Front cover look and feel first. Then we can look at the inside flaps and back cover. I will need to send you text. This is for the full cover. Front. Back. Spine. Inside flaps fro hardcover.

```html
<!DOCTYPE html>
<html lang="en">
<head>
<meta charset="utf-8">
<title>Harvest Soon — Ned Falconby</title>
<link rel="stylesheet" href="https://fonts.googleapis.com/css2?family=Anton&family=Roboto:wght@300;400&display=swap">
<style>
  :root {
    --cover-white: #ffffff;
    --title-red: #d20a0a;
    --title-red-deep: #b80606;
    --ink: #1c1c1c;
    --ink-soft: #3a3a3a;
  }
  html, body {
    margin: 0;
    padding: 0;
    width: 930px;
    height: 1200px;
    overflow: hidden;
    background: var(--cover-white);
  }
  .book-cover {
    position: relative;
    width: 930px;
    height: 1200px;
    background: var(--cover-white);
    overflow: hidden;
  }
  .tagline {
    position: absolute;
    top: 88px;
    left: 0;
    width: 100%;
    margin: 0;
    text-align: center;
    font-family: "Roboto", sans-serif;
    font-weight: 400;
    font-size: 29px;
    color: var(--ink);
    letter-spacing: 0.2px;
  }
  .title-art {
    position: absolute;
    top: 0;
    left: 0;
    width: 930px;
    height: 1200px;
  }
  .title-word {
    font-family: "Anton", sans-serif;
    fill: url(#titleRed);
  }
  .subtitle {
    position: absolute;
    top: 468px;
    left: 0;
    width: 100%;
    margin: 0;
    text-align: center;
    font-family: "Roboto", sans-serif;
    font-weight: 300;
    font-size: 43px;
    line-height: 1.12;
    color: var(--ink-soft);
    text-transform: uppercase;
    letter-spacing: 0.5px;
  }
  .author {
    position: absolute;
    top: 1002px;
    left: 0;
    width: 100%;
    margin: 0;
    text-align: center;
    font-family: "Roboto", sans-serif;
    font-weight: 400;
    font-size: 34px;
    color: var(--ink-soft);
    text-transform: uppercase;
    letter-spacing: 0.5px;
  }
</style>
</head>
<body>
  <main class="book-cover">
    <p class="tagline">Secrets the Bank Teller Keeps Hidden From Clients...</p>

    <svg class="title-art" viewBox="0 0 930 1200" aria-labelledby="bookTitle">
      <title id="bookTitle">Harvest Soon</title>
      <defs>
        <linearGradient id="titleRed" x1="0" y1="0" x2="0" y2="1">
          <stop offset="0" stop-color="var(--title-red)"/>
          <stop offset="1" stop-color="var(--title-red-deep)"/>
        </linearGradient>
      </defs>
      <text class="title-word" x="-6" y="435" font-size="345"
            textLength="942" lengthAdjust="spacingAndGlyphs">HARVEST</text>
      <text class="title-word" x="-6" y="975" font-size="470"
            textLength="942" lengthAdjust="spacingAndGlyphs">SOON</text>
    </svg>

    <h2 class="subtitle">A quiet method for thriving<br>through land holdings</h2>

    <p class="author">Ned Falconby</p>
  </main>
</body>
</html>
```